Skin cancer clinic services trifold brochure

Need trifold brochure listing skin cancer services our clinic provides, staff information, location and brief about skin cancer with colours similar to our web site www.Dermavoy.clinic. I will provide more information regarding services and staff but want this colourful and standout as it will be given to other referring doctors or patients
Updates

Target Market(s)

Age 40 to 80 years

Industry/Entity Type

Medical

Font styles to use
Serif

Colors

Designer to choose colors to be used in the design.

Requirements
Must have
• Logo, services, contact info, beach or sun look and colours similar to web site or logo

```html
<!DOCTYPE html>
<html lang="en">
<head>
<meta charset="utf-8">
<title>Dermavoy Skin Cancer Clinic – Brochure Inside</title>
<link href="https://fonts.googleapis.com/css2?family=Pathway+Gothic+One&family=Mulish:ital,wght@0,300;0,400;0,700;0,800;1,800&display=swap" rel="stylesheet">
<style>
  :root{
    --orange-bg:#E9703A;
    --orange-panel:#EA8935;
    --charcoal:#4A4A4C;
    --accent-orange:#F07E2E;
    --heading-blue:#2E9BDB;
    --text-light:#ECECEC;
    --text-dark:#2E2E2E;
  }
  *{margin:0;padding:0;box-sizing:border-box}
  html,body{width:1200px;height:927px;overflow:hidden;background:var(--orange-bg)}
  .brochure{position:relative;width:1200px;height:927px;overflow:hidden;font-family:"Mulish",sans-serif}
  .backdrop{position:absolute;inset:0;width:1200px;height:927px}
  .section-title{font-family:"Pathway Gothic One",sans-serif;font-weight:400;color:var(--heading-blue);line-height:1;position:absolute}
  .panel-text{position:absolute;text-align:justify;hyphens:auto}

  .staff-photo{position:absolute;left:45px;top:113px;width:317px;height:249px;border:1.5px solid var(--accent-orange);border-radius:34px 34px 34px 34px;background:linear-gradient(135deg,#D8D9DC 0%,#C4C7CC 45%,#8EA3C4 70%,#B9A184 100%)}

  .staff-title{left:27px;top:376px;font-size:35px}
  .staff-intro{left:27px;top:430px;width:353px;font-size:13.1px;font-weight:300;color:var(--text-light);line-height:16.4px}
  .doctor-list{left:27px;top:512px;width:353px;font-size:13.1px;font-weight:300;color:var(--text-light);line-height:16.4px;text-align:left;list-style:none}
  .doctor-name{color:var(--accent-orange);font-weight:700}
  .tagline{position:absolute;left:27px;top:660px;width:360px;font-size:16.2px;font-weight:800;font-style:italic;color:#fff;line-height:20px}
  .staff-outro{left:27px;top:717px;width:353px;font-size:13.1px;font-weight:300;color:var(--text-light);line-height:16.4px}

  .services-title{left:434px;top:177px;font-size:36px}
  .services-text{left:434px;top:231px;width:346px;font-size:11.2px;font-weight:300;color:var(--text-dark);line-height:14.5px}
  .services-text b{font-weight:800;color:#262626}
  .services-text .emph{font-weight:400}

  .treatments-title{left:834px;top:120px;font-size:36px}
  .treatments-text{left:834px;top:175px;width:336px;font-size:13.1px;font-weight:300;color:var(--text-light);line-height:16.4px}
  .treatments-text b{color:var(--accent-orange);font-weight:700}
</style>
</head>
<body>
<main class="brochure">
  <svg class="backdrop" viewBox="0 0 2184 1688" preserveAspectRatio="none" aria-hidden="true">
    <defs>
      <clipPath id="band-shape">
        <path d="M0 170 C250 200 520 265 742 265 C1000 262 1250 160 1466 165 C1720 172 1960 250 2184 285 L2184 1525 C1960 1490 1720 1418 1466 1420 C1250 1422 1000 1525 742 1528 C520 1528 250 1460 0 1420 Z"/>
      </clipPath>
    </defs>
    <rect width="2184" height="1688" fill="var(--orange-bg)"/>
    <g clip-path="url(#band-shape)">
      <rect width="2184" height="1688" fill="var(--charcoal)"/>
      <rect x="742" y="0" width="724" height="1688" fill="var(--orange-panel)"/>
    </g>
  </svg>

  <section class="panel-staff">
    <div class="staff-photo" role="img" aria-label="Photo of a nurse examining a patient's arm in a clinic treatment room"></div>
    <h2 class="section-title staff-title">Our Staff</h2>
    <p class="panel-text staff-intro">At Dermavoy Skin Cancer Clinic, our highly qualified administrative staff, nurses and doctors are an integral part of the team ensuring excellent clinical care is provided to our patients. We currently have 5 experienced local doctors:</p>
    <ul class="panel-text doctor-list">
      <li><span class="doctor-name">Dr. Maren Ashcombe</span>, BMed, FRACGP, Diploma Skin Cancer Medicine/Surgery, Diploma Aesthetic Medicine</li>
      <li><span class="doctor-name">Dr. Priya Vantreth</span>, BMed, FRACGP, Diploma Skin Cancer Medicine/Surgery</li>
      <li><span class="doctor-name">Dr. Colette Brannagh</span>, MBBS, FRACGP</li>
      <li><span class="doctor-name">Dr. Owen Talford</span>, MBBS (Syd), Dip Law</li>
      <li><span class="doctor-name">Dr. Tessa Moorland</span>, MBBS (Hons), FRACGP, Cert. Skin Cancer Medicine</li>
    </ul>
    <p class="tagline">Early detection of skin cancers is vital for the best outcome.</p>
    <p class="panel-text staff-outro">Dermavoy has invested in technology and research to provide the latest diagnostic services and treatments to meet the needs of our patients.</p>
  </section>

  <section class="panel-services">
    <h2 class="section-title services-title">Professional Skin Services</h2>
    <p class="panel-text services-text">
      <b>Advanced Skin Cancer Detection</b> with detailed Full Body skin checks using dermoscopy and technology to minimise unnecessary excisions.<br>
      <b>Individual Mole mapping and full body photography</b> utilising intelligent skin analytics with <b>SkinTrace</b> – an artificial intelligence-powered platform which provides tools for documenting and diagnosing skin cancers and evidence-based care. Powered by AI algorithms, it will identify changes to the skin over time and support early clinical decisions and diagnosis.<br>
      <b>LesionView Skin Imaging System</b> which captures high-quality images using SpectraScan – clinically proven technology which provides a unique level of detail and information from up to 2mm beneath the skin's surface allowing deeper assessment and risk of melanoma.<br>
      <b>Purpose Built Skin Cancer Facility</b> providing Surgical treatments in 2 dedicated fully equipped theatres and Treatment room staffed by skilled skin cancer medicine nurses.<br>
      <b>Large referral basis</b> for our patients that may require extensive therapy for their skin cancers, including Radio<span class="emph">therapy for cosmetically sensitive areas that are not optimally treated with surgery, Advanced care under the Coastal Melanoma Unit or MOHs Surgery and more.</span><br>
      <span class="emph"><b>Priority Spot Checks</b> – appointments are set aside every day for urgent suspicious lesions allowing for quick evaluation, whether for an existing or new patient. Although we welcome GP referrals, it is not required.<br>
      <b>GP Team Approach</b> – Dermavoy believes it is important that an integrated team approach to a patient's skin cancer care is important, and communication of histological results and findings are shared with their GP upon permission.<br>
      <b>Pain minimisation Techniques</b> –Topical numbing creams and ChillPoint numbing agents are available to minimise tenderness that can come with local anaesthetics. Our theatres are equipped with overhead projectors playing calming nature scenes to ensure our patients are comfortable.</span>
    </p>
  </section>

  <section class="panel-treatments">
    <h2 class="section-title treatments-title">Specialised Treatments</h2>
    <p class="panel-text treatments-text">
      <b>Surgical Procedures</b> – Our Doctors are proficient in surgical procedures from simple diagnostic biopsies or elliptical excisions to advanced procedures including skin grafts and surgical flap repair, all under a local anaesthetic.<br>
      <b>Radiatom Radiofrequency procedures</b> – Surgical options include a high frequency radiosurgical device for scalpel-less surgery. It allows our Doctors to use Radiowaves instead of scalpels to provide advanced skin cancer surgical procedures or cosmetic procedures; including removal of spider veins or vascular lesions and benign non-suspicious moles, skin tags, seborrheic keratoses, warts and other raised lesions. A Radiatom procedure ensures minimal thermal tissue damage, bleeding, and recovery time, thus enhancing cosmetic outcome.<br>
      <b>Margin Controlled Surgery</b> (also known as Slow Mohs or Delayed Closure) – a process where aggressive skin cancers are not closed after excision until the histological status and clearance is known. This can minimise the need for larger excisions and potentially benefit cosmetic outcome; especially in cosmetically sensitive regions such as the nose, ears and face.<br>
      <b>Non-surgical treatments and preventative therapy options</b> – Our goal is to prevent and treat skin cancer in the least invasive way possible as appropriate. This includes preventative care including Vitamin B3 benefits and sun safe practices - to topical therapies, such as liquid nitrogen and prescriptive therapy for solar keratoses or superficial Non-Melanoma skin cancers.<br>
      <b>Cosmetic Services</b> – Dermavoy approaches our skin cancer patient holistically and, by appointment, we can offer advice and treatment regarding skin pigmentation, troublesome bumps and lumps and more! Please see our web site at www.Dermavoy.clinic for more information.
    </p>
  </section>
</main>
</body>
</html>
```